Web Design for Independent Pet Supply shop.

Larchmont Critter Depot is a locally owned and operated premium natural pet food store and supply company with 2 thriving retail stores in Bend, Oregon, and a home delivery service. The pet food offered is the best on the market and may be described as “holistic”. Also on offer is a vast selection of toys, training tools, treats, and other supplies, as well as dog washing services that range from "do-it yourself" to "spa." Current site: LarchmontCritterDepot.com. They need a new, updated and responsive site.
Likes:
Vondals.com: Natural colors, not loud, pages in motion, simple & clean but very informative.
Tobiasmerrow.com: Everything in simple big colorful blocks. The specials run across the top and in motion. This site looks very professional but simple. The information is available several different places.
Greenbarrel.com: Again big blocks through out. Very Fun and inviting. Tons of information with videos and recipes and testimonials. Pleasant feel and colors as well.
Dislikes:
Furvana.com: Looks cheap, hate the colors, very busy and over whelming. Hate the old style header bar going across with options. Too many printed words instead of fun images.
Colors should be "natural" tones, warm and soothing. Deep dark blue and greys with earthy wood color.
Do Not Use: Blue violet, violet, red violet

```html
<!DOCTYPE html>
<html lang="en">
<head>
<meta charset="utf-8">
<title>Larchmont Critter Depot</title>
<link href="https://fonts.googleapis.com/css2?family=Open+Sans:wght@400;600;700;800&display=swap" rel="stylesheet">
<style>
:root{
  --navy:#0d2b68;
  --navy-deep:#0a2257;
  --wood:#cf7a3f;
  --wood-dark:#c06a30;
  --ink:#333;
  --muted:#666;
  --line:#e2e2e2;
  --grey-panel:#e6e6e6;
  --white:#fff;
}
*{box-sizing:border-box;margin:0;padding:0}
html,body{width:769px;height:1200px;overflow:hidden}
body{position:relative;font-family:"Open Sans",sans-serif;color:var(--ink);
  background:linear-gradient(180deg,#c9733b 0%,#d08754 30%,#ecc4a7 52%,#fff 70%,#fff 100%)}
.abs{position:absolute}
.page{position:absolute;left:64px;top:61px;width:641px;height:1040px;background:transparent}
.header{position:absolute;left:64px;top:61px;width:641px;height:105px;background:var(--white)}
.brand{position:absolute;left:7px;top:56px;display:flex;align-items:center;gap:5px;
  font-weight:800;font-size:13.5px;color:var(--wood-dark);letter-spacing:.2px}
.brand-dot{width:16px;height:16px;border-radius:50%;background:var(--wood)}
.utility{position:absolute;right:12px;top:30px;display:flex;align-items:center;gap:14px;font-size:8.5px;color:#444}
.utility span{display:flex;align-items:center;gap:4px}
.cart{display:flex;align-items:stretch;height:22px;background:#e4e4e4;font-size:8.5px}
.cart-icon{width:26px;background:var(--wood);display:flex;align-items:center;justify-content:center}
.cart-label{padding:0 10px;display:flex;align-items:center}
.nav{position:absolute;left:194px;top:74px;display:flex;gap:0;font-size:8.5px;color:#444}
.nav a{text-decoration:none;color:inherit;margin-right:23px;position:relative;padding-bottom:6px}
.nav a:last-child{margin-right:0}
.nav a.active{color:var(--navy);font-weight:600}
.nav a.active::after{content:"";position:absolute;left:0;right:0;bottom:-1px;height:2px;background:var(--navy)}
.hero-photo{position:absolute;left:64px;top:166px;width:442px;height:287px;
  background:linear-gradient(135deg,#e9e9eb 0%,#cfcfd3 45%,#8a8f9c 70%,#c7b9a8 100%)}
.hero-panel{position:absolute;left:506px;top:166px;width:199px;height:287px;
  background:linear-gradient(180deg,#0f3173,var(--navy-deep));color:var(--white)}
.hero-panel::before{content:"";position:absolute;left:-8px;top:136px;border:8px solid transparent;border-left:0;border-right-color:var(--navy)}
.hero-title{position:absolute;top:22px;left:0;width:100%;text-align:center;font-weight:800;font-size:13px;line-height:16px;letter-spacing:.6px}
.hero-rule{position:absolute;left:37px;top:62px;width:128px;height:2px;background:var(--white)}
.hero-rule::after{content:"";position:absolute;left:58px;top:1px;border:5px solid transparent;border-top-color:var(--white);border-bottom:0}
.perk{position:absolute;left:16px;display:flex;gap:9px;align-items:center}
.perk h3{font-size:11px;font-weight:600;letter-spacing:.2px}
.perk p{font-size:7.5px;font-weight:600}
.section-title{position:absolute;left:70px;top:472px;font-size:11.5px;font-weight:600;color:var(--navy);letter-spacing:.2px}
.section-title::after{content:"";position:absolute;left:0;top:19px;width:37px;height:2px;background:var(--navy)}
.product-band{position:absolute;left:64px;top:453px;width:641px;height:229px;background:var(--white)}
.card{position:absolute;top:512px;width:134px;height:120px;border:1px solid var(--line);background:var(--white);box-shadow:0 1px 2px rgba(0,0,0,.08)}
.card .thumb{position:absolute;left:12px;top:14px;right:12px;bottom:14px;border-radius:4px}
.sale{position:absolute;right:4px;top:6px;width:24px;height:24px;border-radius:50%;background:#f2f2f2;border:1px solid #ddd;
  font-size:6px;font-weight:600;display:flex;align-items:center;justify-content:center;color:#333}
.card-label{position:absolute;top:638px;font-size:9.5px;color:var(--muted);letter-spacing:.3px}
.arrow{position:absolute;top:559px;font-size:16px;color:var(--wood-dark)}
.service{position:absolute;top:682px;width:160px;height:160px;color:var(--white);padding:14px 9px}
.service h2{font-size:14px;font-weight:800;letter-spacing:1px;margin-bottom:10px}
.service p{font-size:8px;font-weight:600;line-height:12.8px}
.btn-outline{display:inline-block;margin-top:12px;border:1.5px solid var(--white);padding:2px 5px;font-size:8px;font-weight:600;color:var(--white)}
.service.navy{background:var(--navy)}
.service.wood{background:var(--wood)}
.service-photo{position:absolute;top:682px;width:160px;height:160px}
.testimonial{position:absolute;left:65px;top:842px;width:320px;height:159px;background:linear-gradient(180deg,#f0f0f0,#dcdcdc);text-align:center}
.testimonial h2{margin-top:17px;font-size:13.5px;font-weight:800;color:var(--navy);letter-spacing:1px}
.quote-mark{font-size:26px;font-weight:800;color:var(--navy);line-height:20px;margin-top:4px}
.testimonial p{font-size:7.8px;line-height:12.8px;color:#444;padding:0 30px;margin-top:6px}
.btn-navy{display:inline-block;margin-top:10px;border:1.5px solid var(--navy);padding:2px 5px;font-size:8px;font-weight:600;color:var(--navy)}
.video{position:absolute;left:385px;top:842px;width:320px;height:159px;
  background:linear-gradient(120deg,#8fb0c8 0%,#c9b48c 40%,#e3d3b0 60%,#7c9bb3 100%)}
.play{position:absolute;left:134px;top:55px}
.footer-col{position:absolute;top:1028px;font-size:8px;color:#555;line-height:12px}
.footer-col h4{font-size:10.5px;font-weight:800;color:var(--navy);letter-spacing:.8px;margin-bottom:14px;position:relative}
.footer-col h4::after{content:"";position:absolute;left:0;top:18px;width:37px;height:2px;background:var(--navy)}
.footer-col ul{list-style:none}
.footer-col li{margin-bottom:2px}
.footer-col li::before{content:"•";color:#999;margin-right:5px}
.email-field{margin-top:10px;width:145px;height:21px;border:1px solid #ccc;background:#eee;font-size:7.5px;color:#999;padding:4px 7px}
.btn-wood{display:inline-block;margin-top:10px;background:var(--wood);color:var(--white);font-size:8px;padding:5px 9px}
.pay-grid{display:grid;grid-template-columns:repeat(3,max-content);gap:8px 6px;align-items:center}
.pay{height:14px;border-radius:2px}
.bottom-bar{position:absolute;left:0;top:1172px;width:769px;height:28px;background:var(--navy-deep);color:var(--white);
  font-size:7.5px;display:flex;align-items:center;justify-content:center}
</style>
</head>
<body>

<header class="header">
  <div class="brand"><span class="brand-dot"></span>Larchmont Critter Depot</div>
  <div class="utility">
    <span><svg width="7" height="9" viewBox="0 0 7 9"><rect x="0" y="4" width="7" height="5" rx="1" fill="#cf7a3f"/><path d="M1.5 4V2.5a2 2 0 014 0V4" stroke="#cf7a3f" fill="none"/></svg>login</span>
    <span><svg width="9" height="9" viewBox="0 0 9 9"><circle cx="4" cy="2.5" r="2" fill="#cf7a3f"/><path d="M0 9c0-3 8-3 8 0z" fill="#cf7a3f"/></svg>Create an account</span>
    <div class="cart"><div class="cart-icon"><svg width="13" height="11" viewBox="0 0 13 11"><path d="M1 3h11l-1.5 7h-8z" fill="none" stroke="#fff" stroke-width="1.3"/><path d="M4 3l2-2.5M9 3L7 .5" stroke="#fff"/></svg></div><div class="cart-label">Shoping Cart</div></div>
  </div>
  <nav class="nav">
    <a class="active">Home</a><a>Events</a><a>Blog</a><a>About</a><a>Dog Wash</a><a>Products</a><a>Resources</a><a>Links</a><a>Contact</a>
  </nav>
</header>

<div class="hero-photo" role="img" aria-label="Smiling couple hugging a large tricolor dog against a light backdrop"></div>
<aside class="hero-panel">
  <div class="hero-title">PET ANCIENT ODEN<br>UNITS AND FOOD</div>
  <div class="hero-rule"></div>
  <div class="perk" style="top:91px">
    <svg width="32" height="28" viewBox="0 0 32 28" fill="none" stroke="#fff" stroke-width="2"><circle cx="8" cy="8" r="6"/><path d="M8 5v3l2 2"/><path d="M14 10h8v12H4v-8M22 14h5l3 4v4h-8"/><circle cx="9" cy="23" r="2.5" fill="#0d2b68"/><circle cx="25" cy="23" r="2.5" fill="#0d2b68"/></svg>
    <div><h3>FREE SHIPING</h3><p>Only for our special offers</p></div>
  </div>
  <div class="perk" style="top:151px">
    <svg width="32" height="28" viewBox="0 0 32 28" fill="none" stroke="#fff" stroke-width="2"><path d="M2 6h4l4 14h14l3-10H9"/><circle cx="12" cy="25" r="2"/><circle cx="22" cy="25" r="2"/><path d="M15 3a5 5 0 015 5M20 8l-2-1M20 8l1-2"/></svg>
    <div><h3>FREE RETURN</h3><p>Free Return for 100 Days</p></div>
  </div>
  <div class="perk" style="top:203px">
    <svg width="32" height="28" viewBox="0 0 32 28" fill="none" stroke="#fff" stroke-width="2"><path d="M2 8h4l4 12h16l3-12H7"/><path d="M10 12h16M11 16h14"/><rect x="12" y="2" width="5" height="5"/><rect x="19" y="1" width="6" height="6"/><circle cx="12" cy="24" r="2"/><circle cx="24" cy="24" r="2"/></svg>
    <div><h3>ALL ITEMS IN STOCK</h3><p>Free Return for 100 Days</p></div>
  </div>
</aside>

<section class="product-band"></section>
<h2 class="section-title">FEATURED PRODUCT</h2>
<span class="arrow" style="left:71px">‹</span>
<span class="arrow" style="left:689px">›</span>

<div class="card" style="left:85px"><div class="thumb" role="img" aria-label="Dog training collar with two remote units" style="background:linear-gradient(135deg,#f4f0ec,#a89a8c,#5a4a40)"></div><span class="sale">SALE</span></div>
<div class="card" style="left:238px"><div class="thumb" role="img" aria-label="Rope and wood chew toys" style="background:linear-gradient(135deg,#fbf6ee,#e3c79c,#8a94b8,#fbf6ee)"></div></div>
<div class="card" style="left:392px"><div class="thumb" role="img" aria-label="Box of bacon flavoured dog chews" style="background:linear-gradient(135deg,#f7eeea,#b03a36,#d9a670)"></div><span class="sale">SALE</span></div>
<div class="card" style="left:546px"><div class="thumb" role="img" aria-label="Bag of dry dog food" style="background:linear-gradient(135deg,#f9f5e0,#f0c21e,#d6402a)"></div><span class="sale">SALE</span></div>
<span class="card-label" style="left:85px">Lorem Ipsum</span>
<span class="card-label" style="left:240px">Lorem Ipsum</span>
<span class="card-label" style="left:394px">Lorem Ipsum</span>
<span class="card-label" style="left:549px">Lorem Ipsum</span>

<article class="service navy" style="left:65px">
  <h2>DOG WASHING</h2>
  <p>Lorem ipsum dolor sit amet, eiusmod tempor incididunt ut labore et dolore magna aliqua. Ut laboris nisi ut aliquip ex ea commodo consequat.</p>
  <span class="btn-outline">Read More</span>
</article>
<div class="service-photo" style="left:225px;background:linear-gradient(135deg,#d9cfc6,#a5622e,#efe9e2)" role="img" aria-label="Brown dog being lathered with soap during a bath"></div>
<article class="service wood" style="left:385px">
  <h2>DOG SPA</h2>
  <p>Lorem ipsum dolor sit amet, eiusmod tempor incididunt ut labore et dolore magna aliqua. Ut laboris nisi ut aliquip ex ea commodo consequat.</p>
  <span class="btn-outline">Read More</span>
</article>
<div class="service-photo" style="left:545px;background:linear-gradient(135deg,#2f3336,#3e4346,#9a7a55,#2a2d30)" role="img" aria-label="Small dog being brushed against a dark background"></div>
<svg class="abs" style="left:225px;top:754px" width="8" height="16"><path d="M0 0l8 8-8 8z" fill="#0d2b68"/></svg>
<svg class="abs" style="left:545px;top:754px" width="8" height="16"><path d="M0 0l8 8-8 8z" fill="#cf7a3f"/></svg>

<section class="testimonial">
  <h2>TESTIMONIAL</h2>
  <div class="quote-mark">”</div>
  <p>Lorem ipsum dolor sit amet, consectetur adipiscing elit, sed do eiusmod tempor incididunt ut labore et &nbsp;minim veniam, quis nostrud exercitation ullamco laboris nisi ut reprehenderit in voluptate velit esse cillum dolore pariatur.</p>
  <span class="btn-navy">Read More</span>
</section>
<div class="video" role="img" aria-label="Video still of a woman with two golden retrievers by the sea">
  <svg class="play" width="52" height="52" viewBox="0 0 52 52"><circle cx="26" cy="26" r="24" fill="none" stroke="#fff" stroke-width="3"/><path d="M20 15l17 11-17 11z" fill="#fff"/></svg>
</div>

<footer>
  <div class="footer-col" style="left:66px">
    <h4>OUR STORE</h4>
    <p>123 Lorem ipsum,Dole sit city<br>124587 Consitecture</p>
    <p style="margin-top:6px">1548 632 5480</p>
    <p style="margin-top:6px">info@larchmontcritterdepot.com</p>
  </div>
  <div class="footer-col" style="left:238px">
    <h4>USER</h4>
    <ul><li>Login</li><li>View Cart</li><li>Terms &amp; Condition</li><li>Privacy Policy</li><li>Shipping Policy</li></ul>
  </div>
  <div class="footer-col" style="left:369px;width:150px">
    <h4>SUBSCRIPTION</h4>
    <p>Subscribe for our e-news Letter and received latest products update and promotions.</p>
    <div class="email-field">enter Your email address</div>
    <span class="btn-wood">Subscribe</span>
  </div>
  <div class="footer-col" style="left:567px">
    <h4>SECURE PAYMENT</h4>
    <div class="pay-grid">
      <div class="pay" style="width:34px;background:#1a3a8c"></div>
      <div class="pay" style="width:26px;border-radius:50%;background:#3b6fb6"></div>
      <div class="pay" style="width:26px;border-radius:50%;background:#e0502a"></div>
      <div class="pay" style="width:22px;background:#2c4a9a"></div>
      <div class="pay" style="width:60px;background:#6f9c3a;grid-column:span 2"></div>
      <div class="pay" style="width:50px;height:20px;background:#1a3a8c"></div>
      <div class="pay" style="width:56px;height:20px;background:#e0502a;grid-column:span 2"></div>
    </div>
  </div>
</footer>

<div class="bottom-bar">Copyright © 2014. All Rights Reserved</div>
</body>
</html>
```